Book Cover- KEEPSAKES Coming of Age near Tallow Creek, Nebraska: One Quiet Prairie River Hamlet

Lantern Field Publishing is publishing a book
Book Title: KEEPSAKES Coming of Age near Tallow Creek, Nebraska
Subtitle: One Quiet Prairie River Hamlet
Author: Dana Whitcombe
This is a serious of stories and reflections of the author's experiences growing up in small town called Tallow Creek, Colorado.

Front Cover Brief: We would like to have the first picture uploaded below - picture of mountains with fireworks included in the front cover design
Please include
Author Name: Dana Whitcombe

Back Cover Brief: The second image of the road included in the back cover design.
Please include the text- by: Dana Whitcombe.
Along with this text:

Tallow Creek is miraculous. Being touched by the magic of this beautiful place is my motivation to share the experience.

I was blessed to grow up in a beautiful town and was raised by a loving family during an amazing time of global change. Shared experiences are an exceptional way for us all to learn, grow, and be entertained. I hope you enjoy the stories as much as I enjoyed writing them. After all, the name of Tallow Creek could well be “Magic.”

This book is a collection of memories and shared experiences from growing up with friends and family in One Quiet Prairie River Hamlet. These recollections were written from a place in my heart where love lives. I loved growing up in Tallow Creek.

KEEPSAKES Coming Of Age Near Tallow Creek, Nebraska, is my effort to encourage others to reflect and share their experiences of growing up, wherever that may have been.

If space allows include the name of the publishing company: Lantern Field Publishing on back cover

Spine - We also need a spine with the title of the book Coming of Age near Tallow Creek, Nebraska : One Quiet PRAIRIE River Hamlet and Author's name - Dana Whitcombe.

```html
<!DOCTYPE html>
<html lang="en">
<head>
<meta charset="utf-8">
<title>KEEPSAKES Coming of Age near Tallow Creek, Nebraska – Cover Wrap</title>
<link rel="stylesheet" href="https://fonts.googleapis.com/css2?family=PT+Sans:wght@400;700&family=PT+Sans+Narrow:wght@400;700&display=swap">
<style>
  :root {
    --sky-deep: #2468cf;
    --sky-mid: #4a90de;
    --sky-pale: #a9d0f0;
    --spine-deep: #1f5fc0;
    --spine-light: #4f98e4;
    --title-gold: #f6d99b;
    --subtitle-navy: #1d3f7c;
    --blurb-ink: #15263f;
    --white: #ffffff;
    --road-dark: #3c4a5c;
    --road-mist: #c9d6e3;
    --valley-rose: #b7877a;
    --valley-green: #35503f;
  }
  * { margin: 0; padding: 0; box-sizing: border-box; }
  html, body { width: 1200px; height: 872px; overflow: hidden; background: #ffffff; }
  .cover-wrap { position: relative; width: 1200px; height: 872px; overflow: hidden; font-family: "PT Sans", sans-serif; }

  .back-cover {
    position: absolute; left: 0; top: 0; width: 581px; height: 872px;
    background: linear-gradient(180deg, var(--sky-deep) 0%, var(--sky-mid) 38%, var(--sky-pale) 68%, var(--sky-pale) 100%);
  }
  .back-photo {
    position: absolute; left: 0; top: 557px; width: 581px; height: 315px;
    background: linear-gradient(180deg, var(--sky-pale) 0%, #5d7ea8 22%, var(--road-mist) 46%, #9aa2a6 62%, var(--road-dark) 100%);
  }
  .back-author {
    position: absolute; left: 0; width: 581px; top: 102px; text-align: center;
    color: var(--white); font-weight: 700; font-size: 33px; letter-spacing: 0.5px;
  }
  .back-blurb {
    position: absolute; left: 106px; top: 204px; width: 392px;
    font-family: "PT Sans Narrow", sans-serif; font-size: 16px; line-height: 20px; color: var(--blurb-ink);
  }
  .back-blurb p { margin-bottom: 8px; }
  .publisher {
    position: absolute; left: 0; width: 581px; top: 801px; text-align: center;
    color: var(--white); font-size: 15.5px;
  }

  .spine {
    position: absolute; left: 581px; top: 0; width: 53px; height: 872px;
    background: linear-gradient(90deg, var(--spine-deep) 0%, var(--spine-light) 55%, var(--spine-deep) 100%);
  }
  .spine-author {
    position: absolute; left: 10px; top: 96px; width: 34px; height: 290px;
    writing-mode: vertical-rl; color: var(--white);
    font-weight: 700; font-size: 21px; letter-spacing: 0.5px; line-height: 34px;
  }
  .spine-title {
    position: absolute; left: 3px; top: 424px; width: 48px; height: 420px;
    writing-mode: vertical-rl; color: var(--white); line-height: 23px;
  }
  .spine-title .main { display: block; font-weight: 700; font-size: 14.5px; letter-spacing: 0.3px; }
  .spine-title .sub { display: block; font-size: 17px; letter-spacing: 0.5px; }

  .front-cover {
    position: absolute; left: 634px; top: 0; width: 566px; height: 872px;
    background: linear-gradient(180deg, #2f78d4 0%, var(--sky-mid) 30%, #8fc0ec 55%, var(--sky-pale) 70%);
  }
  .front-photo {
    position: absolute; left: 0; top: 485px; width: 566px; height: 387px;
    background: linear-gradient(180deg, rgba(169,208,240,0) 0%, #9ea9c8 14%, var(--valley-rose) 38%, #6c6b62 58%, var(--valley-green) 80%, #253b2d 100%);
  }
  .front-author {
    position: absolute; left: 0; width: 566px; top: 102px; text-align: center;
    color: var(--white); font-weight: 700; font-size: 33px; letter-spacing: 0.5px;
  }
  .front-title {
    position: absolute; left: 0; width: 566px; top: 212px; text-align: center;
    color: var(--title-gold); font-weight: 700;
  }
  .front-title .lead { display: block; font-size: 66px; line-height: 70px; }
  .front-title .middle { display: block; font-size: 22px; line-height: 34px; }
  .front-title .place { display: block; font-size: 66px; line-height: 70px; }
  .front-subtitle {
    position: absolute; left: 0; width: 566px; top: 388px; text-align: center;
    color: var(--subtitle-navy); font-family: "PT Sans Narrow", sans-serif; font-size: 29px;
  }
</style>
</head>
<body>
<div class="cover-wrap">
  <section class="back-cover">
    <div class="back-photo" role="img" aria-label="Photograph of a straight two-lane road running toward misty blue hills under a clear sky"></div>
    <h2 class="back-author">DANA WHITCOMBE</h2>
    <div class="back-blurb">
      <p>Tallow Creek is miraculous. Being touched by the magic of this beautiful place is my motivation to share the experience.</p>
      <p>I was blessed to grow up in a beautiful town and was raised by a loving family during an amazing time of global change. Shared experiences are an exceptional way for us all to learn, grow, and be entertained. I hope you enjoy the stories as much as I enjoyed writing them. After all, the name of Tallow Creek could well be “Magic.”</p>
      <p>This book is a collection of memories and shared experiences from growing up with friends and family in a quiet prairie river hamlet. These recollections were written from a place in my heart where love lives. I loved growing up in Tallow Creek.</p>
      <p>KEEPSAKES Coming Of Age Near Tallow Creek, Nebraska, is my effort to encourage others to reflect and share their experiences of growing up, wherever that may have been.</p>
    </div>
    <p class="publisher">Lantern Field Publishing</p>
  </section>

  <section class="spine">
    <div class="spine-author">DANA WHITCOMBE</div>
    <div class="spine-title">
      <span class="main">COMING OF AGE NEAR TALLOW CREEK, NEBRASKA:</span>
      <span class="sub">One Quiet Prairie River Hamlet</span>
    </div>
  </section>

  <section class="front-cover">
    <div class="front-photo" role="img" aria-label="Photograph of a valley town at dusk with red cliffs, pine forest and golden fireworks bursting near snowy peaks"></div>
    <h2 class="front-author">DANA WHITCOMBE</h2>
    <h1 class="front-title">
      <span class="lead">KEEPSAKES</span>
      <span class="middle">COMING OF AGE NEAR TALLOW CREEK,</span>
      <span class="place">NEBRASKA:</span>
    </h1>
    <p class="front-subtitle">One Quiet Prairie River Hamlet</p>
  </section>
</div>
</body>
</html>
```